Business Card Design Project

TRX Solutions is a Electrical and Communications Services and Maintenance contractor to the Mining Oil and Gas sectors of Australia.
Our clients will be planners, Schedulers, Tradespeople and Engineers

We are yet to determine the primary colours that we will use on the business cards but the logos attached will form foundation of the colours used for logos on Business cards, Website, Uniforms, vehicles etc.

Target Market(s)

Mining engineers and shedulers

Industry/Entity Type

Contractor

Requirements
Must have
• information to be included on the card

Name: Derek Hanley
Title: Managing Director
Company: TRX Solutions Pty Ltd
Phone: 08 9XXX XXXX
Mobile 0400 318 942
email: dhanley@trxsolutionsgroup.com.au
Website www.trxsolutionsgroup.com.au

Address: U5/14 Kettering Street Malaga, WA 6090
Postal Address: PO Box 7183 Malaga WA 6944

Nice to have
• Double sided. Maybe the logo on the back

```html
<!DOCTYPE html>
<html lang="en">
<head>
<meta charset="utf-8">
<title>TRX Solutions – Business Card</title>
<link href="https://fonts.googleapis.com/css2?family=Fira+Sans+Extra+Condensed:wght@300&family=Questrial&display=swap" rel="stylesheet">
<style>
  :root {
    --page: #ffffff;
    --navy-core: #0e2f57;
    --navy-mid: #0d2547;
    --navy-edge: #0c1b36;
    --orange: #ee7f27;
    --white: #ffffff;
    --rule: rgba(255, 255, 255, 0.55);
    --font-body: "Fira Sans Extra Condensed", "Arial Narrow", sans-serif;
    --font-display: "Questrial", "Century Gothic", sans-serif;
  }
  * { margin: 0; padding: 0; box-sizing: border-box; }
  html, body {
    width: 900px;
    height: 1200px;
    overflow: hidden;
    background: var(--page);
  }
  .sheet {
    position: relative;
    width: 900px;
    height: 1200px;
  }
  .card {
    position: absolute;
    left: 182px;
    width: 542px;
    height: 353px;
    background: radial-gradient(ellipse at 50% 45%, var(--navy-core) 0%, var(--navy-mid) 50%, var(--navy-edge) 100%);
    color: var(--white);
    overflow: hidden;
  }
  .card--front { top: 149px; }
  .card--back { top: 689px; }

  .job-title {
    position: absolute;
    top: 26px;
    width: 100%;
    text-align: center;
    font-family: var(--font-body);
    font-weight: 300;
    font-size: 16px;
  }
  .name-band {
    position: absolute;
    top: 53px;
    left: 0;
    width: 100%;
    height: 39px;
    background: var(--orange);
    display: flex;
    align-items: center;
    justify-content: center;
  }
  .name {
    font-family: var(--font-display);
    font-weight: 400;
    font-size: 27px;
    letter-spacing: 0.3px;
  }
  .divider {
    position: absolute;
    left: 271px;
    top: 121px;
    width: 1px;
    height: 187px;
    background: var(--rule);
  }
  .contact-block {
    position: absolute;
    top: 165px;
    font-family: var(--font-body);
    font-weight: 300;
    font-size: 17px;
    line-height: 29.5px;
    text-align: center;
    list-style: none;
    white-space: nowrap;
  }
  .contact-block--address { left: 0; width: 271px; }
  .contact-block--numbers { left: 272px; width: 270px; }
  .website {
    position: absolute;
    top: 322px;
    width: 100%;
    text-align: center;
    font-family: var(--font-display);
    font-size: 15.5px;
    letter-spacing: 0.4px;
  }

  .brand-name {
    position: absolute;
    top: 50%;
    left: 0;
    width: 100%;
    transform: translateY(-50%);
    text-align: center;
    font-family: var(--font-display);
    font-weight: 400;
    font-size: 40px;
    color: var(--white);
    letter-spacing: 1px;
    white-space: nowrap;
  }
</style>
</head>
<body>
<main class="sheet">
  <section class="card card--front" aria-label="Business card front">
    <p class="job-title">Managing director</p>
    <div class="name-band"><h1 class="name">Derek Hanley</h1></div>
    <ul class="contact-block contact-block--address">
      <li>TRX Solutions Pty Ltd</li>
      <li>U5/14 Kettering Street Bayswater, WA 6053</li>
      <li>PO Box 7183 Bayswater WA 6933</li>
    </ul>
    <div class="divider"></div>
    <ul class="contact-block contact-block--numbers">
      <li>M: 0400 318 942</li>
      <li>P: 08 9XXX XXXX</li>
      <li>E: dhanley@trxsolutionsgroup.com.au</li>
    </ul>
    <p class="website">www.trxsolutionsgroup.com.au</p>
  </section>

  <section class="card card--back" aria-label="Business card back">
    <p class="brand-name">TRX Solutions</p>
  </section>
</main>
</body>
</html>
```